【依頼の目的/概要】
電子書籍(plumet)の表紙デザインをお願いします。

【画像サイズ】
表紙ファイルの理想的な寸法は2,560×1,600ピクセルです。

【タイトル】
あの窓辺にまた灯りがともる静かな暮らしの場を一から育てるための手引き

サブキャッチ
~住む人の歩みを一緒に編み直す語らい中心の新しい手法~

【著者】
株式会社MRTOV
代表取締役 江坂 なつえ

【本の内容】
誰もが迎える老いのステージを「自分の人生まんざらでもなかったなぁ」と思っていただける新手法ナラティブアプローチの方法を介護哲学と共に解説しています。

*本文を参考資料として添付します。

【デザイン要望】
特にイメージにこだわりはありませんので、自由な発想でのデザインご応募を楽しみにしています。
*次点、次次点の方への参加報酬を設定いたしました。
*その他、必要な情報がありましたらお問い合わせください。

暖かいイメージが伝わってきます。
一番人気でした。

この度は力作を多数ご提案いただき、有難うございました。
初めてワクトリアを利用させていただいたのですが、たくさんの洗練されたご提案があったこと、はるかに自分の予想を上回りました。
これからも、利用させていただきたいと思いますので、よろしくお願いいたします。

```html
<!DOCTYPE html>
<html lang="ja">
<head>
<meta charset="utf-8">
<title>あの窓辺にまた灯りがともる — 表紙</title>
<link rel="stylesheet" href="https://fonts.googleapis.com/css2?family=Shippori+Mincho:wght@500;700;800&family=Noto+Sans+JP:wght@500;700&display=swap">
<style>
  :root {
    --paper: #ffffff;
    --rose: #cf5d8e;
    --ink: #3a3a3a;
    --ink-deep: #1e1e1e;
    --sky-light: #e4f3fa;
    --sky: #bfe2f2;
    --blush: #f4c9d8;
  }
  html, body {
    margin: 0;
    padding: 0;
    overflow: hidden;
    background: var(--paper);
  }
  .cover {
    position: relative;
    width: 752px;
    height: 1200px;
    background: var(--paper);
    overflow: hidden;
    font-family: "Shippori Mincho", serif;
    color: var(--ink);
  }
  .title-main {
    position: absolute;
    top: 18px;
    right: 28px;
    height: 860px;
    margin: 0;
    writing-mode: vertical-rl;
    font-family: "Shippori Mincho", serif;
    font-weight: 700;
    font-size: 96px;
    line-height: 1.22;
    color: var(--rose);
    letter-spacing: 0.02em;
  }
  .title-main span { display: block; }
  .title-tail {
    position: absolute;
    top: 44px;
    left: 50px;
    margin: 0;
    font-family: "Noto Sans JP", sans-serif;
    font-weight: 700;
    font-size: 34px;
    line-height: 1.45;
    color: var(--ink);
  }
  .title-tail span { display: block; }
  .author {
    position: absolute;
    top: 300px;
    left: 50px;
    margin: 0;
    font-family: "Shippori Mincho", serif;
    font-weight: 800;
    color: var(--ink-deep);
  }
  .author-company {
    display: block;
    font-size: 24px;
    line-height: 1.4;
  }
  .author-role {
    display: block;
    font-size: 22px;
    margin-top: 6px;
  }
  .author-name {
    font-size: 44px;
    margin-left: 14px;
    letter-spacing: 0.04em;
  }
  .hands-illustration {
    position: absolute;
    left: 75px;
    top: 478px;
    width: 400px;
    height: 400px;
    border-radius: 50%;
    background: radial-gradient(circle at 50% 45%, var(--blush) 0 14%, var(--sky-light) 30%, var(--sky) 100%);
  }
  .subcatch {
    position: absolute;
    left: 90px;
    top: 876px;
    margin: 0;
    font-family: "Shippori Mincho", serif;
    font-weight: 700;
    font-size: 50px;
    line-height: 1.18;
    color: var(--ink);
  }
  .subcatch .line { display: block; }
  .subcatch .line-second { padding-left: 40px; }
  .subcatch .bracket { color: var(--rose); }
  .approach {
    position: absolute;
    left: 0;
    right: 0;
    top: 1020px;
    margin: 0;
    text-align: center;
    font-family: "Shippori Mincho", serif;
    font-weight: 800;
    font-size: 63px;
    line-height: 1.2;
    color: var(--ink-deep);
  }
</style>
</head>
<body>
  <main class="cover">
    <h1 class="title-main">
      <span>あの窓辺にまた</span>
      <span>灯りがともる</span>
    </h1>

    <p class="title-tail">
      <span>静かな暮らしの場を</span>
      <span>一から育てるための</span>
      <span>手引き</span>
    </p>

    <p class="author">
      <span class="author-company">株式会社MRTOV</span>
      <span class="author-role">代表取締役<span class="author-name">江坂 なつえ</span></span>
    </p>

    <div class="hands-illustration" role="img" aria-label="水彩の淡い水色の円の中で、両手がピンクのハートを包み込むイラスト"></div>

    <p class="subcatch">
      <span class="line"><span class="bracket">「</span>住む人の歩みを</span>
      <span class="line line-second">一緒に編み直す<span class="bracket">」</span></span>
    </p>

    <p class="approach">語らい中心の新しい手法</p>
  </main>
</body>
</html>
```